Menu Revamp- Simplify and highlight

Redesign the current menu while maintaining the existing dimensions to fit within a window display. The goal is to improve readability, declutter the layout, and make price visibility more subtle while ensuring the design remains easy to update annually.

Current Challenges:
• The menu feels cluttered, making it difficult for customers to quickly find what they want.
• Prices stand out too much, drawing more attention than necessary.
• Editing and updating the menu each year is cumbersome and needs simplification.

Requirements:
• Maintain the current specifications and dimensions to ensure it fits in the designated window space.
• Improve readability by organizing the menu in a cleaner, more structured format.
• Adjust the price formatting so it is visible but not the primary focus.
• Ensure the new design allows for easy annual updates, minimizing the need for complete redesigns each year.
• Consider a font and layout that enhance clarity while maintaining the brand’s aesthetic.

Additional Considerations:
• Potential use of color or sectioning to group similar items for better flow.
• A design that aligns with the overall brand identity and customer expectations.
• Digital-friendly formatting for quick edits without affecting the overall structure.

This redesign should make the menu more visually appealing, user-friendly, and practical for future updates while keeping within the original space constraints.
Updates

Gathering more feedback

Target Market(s)

Families and people coming to vacation

Industry/Entity Type

food

Font styles to use
Serif
Sans Serif

Colors
0054AA
0677BA
7BADD7
CADEEF
E8F1F8
F0912C
F2A743
F7CA91
FBE8D2
FDF5EE
EE7325
F08F49
F5BC92
FAE3D3
FDF4ED
EB3D1F
EC4F4E
F09395
F8D3D4
FCEDEE

Requirements
Must have
• all the details, names, and such need to stay. I need it organized better and easier to view and read
Nice to have
• it would be nice if the layers were easier to modify and change year to year.
Should not have
• do not remove details. Please make pricing less prevelant.

```html
<!DOCTYPE html>
<html lang="en">
<head>
<meta charset="utf-8">
<title>Menu</title>
<link href="https://fonts.googleapis.com/css2?family=Poppins:wght@400;500;600;700&display=swap" rel="stylesheet">
<style>
:root{
  --navy:#0b2a52;
  --blue:#0054AA;
  --blue-mid:#0677BA;
  --blue-light:#7BADD7;
  --orange:#EE7325;
  --orange-soft:#F08F49;
  --red:#EB3D1F;
  --red-text:#EC4F4E;
  --ink:#1d1d1f;
  --grey:#9c9c9c;
  --panel:#ececec;
}
*{box-sizing:border-box;margin:0;padding:0}
html,body{width:1200px;height:900px;overflow:hidden;background:var(--navy);font-family:"Poppins",sans-serif;color:var(--ink)}
.menu{position:absolute;left:0;top:25px;width:1200px;height:850px;background:#fff;overflow:hidden}
.beach{position:absolute;left:0;bottom:0;width:100%;height:280px;
  background:linear-gradient(180deg,rgba(255,255,255,0) 0%,#d8eef0 8%,#5fbfc6 13%,#9ad7d8 22%,#d5eeee 45%,#eef6f3 66%,#f3e2cf 80%,#ecd3b8 100%)}
.divider{position:absolute;top:30px;height:770px;border-left:1px dashed #888}
.block{position:absolute}
.bar{position:relative;height:24px;margin-bottom:4px}
.bar-fill{position:absolute;inset:0 0 4px 0;background:var(--blue);border-radius:0 14px 14px 0;
  color:#fff;font-weight:700;font-size:12px;display:flex;align-items:center;justify-content:center;letter-spacing:.2px;
  box-shadow:inset -4px 0 0 #fff, inset -5px 0 0 var(--blue-light)}
.bar::after{content:"";position:absolute;left:0;right:6px;bottom:0;height:4px;background:var(--grey)}
.bar.red .bar-fill{background:var(--red);box-shadow:inset -4px 0 0 #fff, inset -5px 0 0 #F09395}
.bar.split .bar-fill{right:62px;border-radius:0}
.bar-price{position:absolute;right:0;top:0;bottom:4px;width:60px;background:var(--orange);border-radius:0 14px 14px 0;
  color:#fff;font-weight:700;font-size:12px;display:flex;align-items:center;justify-content:center}
.intro{font-size:10px;line-height:1.25}
.item{position:absolute;left:0;right:0}
.item h3{font-size:10.8px;font-weight:700;color:var(--blue);line-height:1.2}
.item.hot h3{color:var(--red-text)}
.item p{font-size:9.8px;line-height:1.2;width:68%}
.item p.wide{width:100%}
.pill{display:inline-block;border-radius:8px;font-size:9.5px;font-weight:700;color:#fff;background:var(--orange);
  padding:0 8px;line-height:14px;min-width:46px;text-align:center}
.item .pill{position:absolute;right:0;top:0}
.sizes{position:absolute;right:0;top:0;display:flex;gap:8px}
.size{width:46px;text-align:center;font-size:9.5px;font-weight:700}
.tag{display:block;border-radius:6px;font-size:6.5px;font-weight:600;color:#fff;line-height:10px;margin-bottom:2px;background:var(--blue)}
.tag.alt{background:var(--orange)}
.rock{position:absolute;left:0;right:0;top:114px;height:76px;background:var(--panel);border-radius:6px;text-align:center}
.rock-title{position:absolute;left:30px;right:40px;top:-4px;height:22px;background:var(--orange);border-radius:0 0 14px 14px;
  color:#fff;font-weight:700;font-size:10.5px;display:flex;align-items:center;justify-content:center}
.rock-sizes{position:absolute;left:40px;top:28px;display:flex;gap:6px}
.rock-sizes div{width:46px;font-size:7.5px;font-weight:600}
.rock-sizes .tag{background:var(--blue-light);font-size:6.5px}
.rock-note{position:absolute;left:0;right:0;top:60px;font-size:7.5px}
.kids{display:grid;grid-template-columns:1fr 1fr;column-gap:14px}
.kids h3{font-size:10.8px;font-weight:700;color:var(--blue)}
.kids p{font-size:9.8px;line-height:1.2;margin-bottom:8px}
.side-row{position:absolute;left:0;right:0;display:flex;align-items:center;font-size:10.5px;font-weight:700}
.side-row .name{width:90px}
.side-row .pill{margin-right:12px}
.side-row .gap{flex:1}
.shakes-title{position:absolute;left:0;right:0;top:142px;text-align:center;font-size:23px;line-height:26px;font-weight:700;color:var(--red)}
.shakes-title::before,.shakes-title::after{content:"";position:absolute;top:50%;width:95px;border-top:1px solid #555}
.shakes-title::before{left:4px}.shakes-title::after{right:18px}
.flavours{position:absolute;left:0;top:668px;width:100%;display:grid;grid-template-columns:1.05fr 1.12fr .83fr;font-size:7.6px;line-height:10.9px;white-space:nowrap}
.flavours div+div{border-left:1px dashed #888;padding-left:4px}
.dots{flex:1;border-bottom:1px dotted #aaa;margin:0 8px}
</style>
</head>
<body>
<div class="menu">
  <div class="beach" role="img" aria-label="Photo of a turquoise sea meeting a sandy beach with foam along the shore"></div>
  <div class="divider" style="left:405px"></div>
  <div class="divider" style="left:793px"></div>

  <!-- Column 1 -->
  <section class="block" style="left:53px;top:0;width:310px;height:850px">
    <div class="bar" style="position:absolute;top:31px;left:0;right:0"><div class="bar-fill">1/4 HAND SMASHED BURGERS</div></div>
    <p class="intro" style="position:absolute;top:77px">All of our burgers are <b>100%</b> hand-smashed ground chuck beef and served on a toasted Artisan bun.</p>
    <div class="rock">
      <div class="rock-title">THE ROCK CHEESEBURGER</div>
      <div class="rock-sizes">
        <div><span class="tag">SINGLE</span>$7.49</div>
        <div><span class="tag">DOUBLE</span>+$1.99</div>
        <div><span class="tag">TRIPLE</span>+$3.98</div>
        <div><span class="tag">QUAD</span>+$5.97</div>
      </div>
      <p class="rock-note">Add Bacon or Shredded Brisket- <b>$1.49/$2.49</b></p>
    </div>
    <div class="item" style="top:211px"><h3>SPINNACKER BARBECUE</h3><p>Bacon, Onion Ring, Cheddar Cheese and Marlo’s® Sassy BBQ Sauce. Make it Spicy with Jalapenos and Queso- <b>$.99</b> | Add Shredded Brisket- <b>$2.49</b></p>
      <div class="sizes"><div class="size"><span class="tag">SINGLE</span>$7.49</div><div class="size"><span class="tag alt">DOUBLE</span>+$1.99</div></div></div>
    <div class="item" style="top:278px"><h3>SOUTH EDEN HAMBURGER</h3><p>Add Bacon or Shredded Brisket <b>$1.49/$2.49</b></p>
      <div class="sizes"><div class="size"><span class="tag">SINGLE</span>$7.49</div><div class="size"><span class="tag alt">DOUBLE</span>+$1.99</div></div></div>
    <div class="item hot" style="top:322px"><h3>GUS’ AVOCADO QUESO</h3><p>Avocado,Tomato, and White Queso Cheese</p>
      <div class="sizes"><div class="size"><span class="tag">SINGLE</span>$7.49</div><div class="size"><span class="tag alt">DOUBLE</span>+$1.99</div></div></div>
    <div class="item hot" style="top:368px"><h3>THE GARDENCITY HOT HONEY</h3><p>Jalapenos, Hot Honey, Pepperjack Cheese, Bacon, Lettuce, Tomato</p>
      <div class="sizes"><div class="size"><span class="tag">SINGLE</span>$7.49</div><div class="size"><span class="tag alt">DOUBLE</span>+$1.99</div></div></div>
    <div class="item hot" style="top:425px"><h3>CISCO BEACH GARLIC PARM</h3><p>Creamy Garlic Parmesean Sauce, Onion, Lettuce</p>
      <div class="sizes"><div class="size"><span class="tag">SINGLE</span>$7.49</div><div class="size"><span class="tag alt">DOUBLE</span>+$1.99</div></div></div>
    <div class="item hot" style="top:472px"><h3>HOT SPRINGS DOUBLE<br>GRILLED CHEESE</h3><p>Two Cheesy Patties, a Grilled Cheese Sandwich, and Classic Burger Toppings in One Burger</p>
      <div class="sizes"><div class="size"><span class="tag">SINGLE</span>$7.49</div><div class="size"><span class="tag alt">DOUBLE</span>+$1.99</div></div></div>
    <div class="bar split" style="position:absolute;top:550px;left:0;right:0"><div class="bar-fill" style="justify-content:flex-start;padding-left:22px">RAINBOW COVE WRAPS</div><div class="bar-price">$8.99</div></div>
    <p class="intro" style="position:absolute;top:609px">All wraps are made to order with fresh grilled chicken or shrimp and rolled in a Tomato Tortilla</p>
    <div class="item hot" style="top:641px"><h3>AVOCADO CHICKEN RANCH</h3><p class="wide">Smoked Chicken, Bacon, Avocado, Lettuce, Spinach and Tomato with Ranch Dressing</p></div>
    <div class="item hot" style="top:686px"><h3>BBQ CHICKEN BACON</h3><p class="wide">Smoked Chicken, Bacon, Cheddar Cheese, Red Onion, Lettuce and Tomato with Marlo’s Raspberry BBQ Sauce</p></div>
    <div class="item hot" style="top:734px"><h3>CHIPOTLE SHRIMP</h3><p class="wide">Fried Shrimp, Tomato and Lettuce with Chili Lime Aioli<br>Add Avocado or Bacon - <b>$.99 / $1.49 ea</b></p></div>
  </section>

  <!-- Column 2 -->
  <section class="block" style="left:443px;top:0;width:314px;height:850px">
    <div class="bar split" style="position:absolute;top:33px;left:0;right:0"><div class="bar-fill">SEASHELL FINDERS (KIDS)</div><div class="bar-price">$7.99</div></div>
    <p class="intro" style="position:absolute;top:79px">Includes Side of Fries or Onion Rings and 12 oz Drink</p>
    <div class="kids" style="position:absolute;top:100px;left:0;right:0">
      <div><h3>LITTLE BURGER</h3><p>Slider size burger with pickles &amp; ketchup. Add cheese for free.</p></div>
      <div><h3>PULLED PORK SANDWICH</h3><p>1/2 of a regular sandwich with sweet raspberry BBQ sauce.</p></div>
      <div><h3>CORN DOG</h3></div>
      <div><h3>GRILLED CHEESE</h3></div>
    </div>
    <div class="bar" style="position:absolute;top:190px;left:0;right:0"><div class="bar-fill">PULLED PORK &amp; SHRIMP</div></div>
    <p class="intro" style="position:absolute;top:231px">Our Pulled Pork is house smoked and slow roasted. All pork and shrimp are served on a Ciabatta bun</p>
    <div class="item" style="top:266px"><h3>SIDDOWAY PUMP PULLED PORK</h3><p>Pulled Pork and Marlo’s® Sweet Raspberry BBQ Sauce</p><span class="pill">$8.49</span></div>
    <div class="item" style="top:311px"><h3>2<sup style="font-size:6px">ND</sup> POINT SWEET PULLED PORK</h3><p>Pulled Pork, Marlo’s® Sweet Raspberry BBQ Sauce and Coleslaw</p><span class="pill">$8.49</span></div>
    <div class="item" style="top:354px"><h3>1<sup style="font-size:6px">ST</sup> POINT SPICY PULLED PORK</h3><p style="width:80%">Pulled Pork, Marlo’s® Sassy BBQ Sauce, Chopped Bacon, Pepperjack Cheese and Jalapenos</p><span class="pill">$8.99</span></div>
    <div class="item" style="top:398px"><h3>FISH HAVEN SHRIMP PO’ BOY</h3><p style="width:80%">Fried Shrimp, Tomato and Lettuce with Chili Lime Aioli | Add Avocado or Bacon - <b>$.99 / $1.49 ea</b></p><span class="pill">$8.99</span></div>
    <div class="bar" style="position:absolute;top:461px;left:0;right:0"><div class="bar-fill">SHREDDED BRISKET</div></div>
    <p class="intro" style="position:absolute;top:503px">Our Shredded Brisket is smoked, braised, and shredded. Served on Ciabatta Buns.</p>
    <div class="item" style="top:539px"><h3>SIDDOWAY PUMP BRISKET</h3><p>Brisket and Marlo’s® Sweet Raspberry BBQ Sauce</p><span class="pill">$9.99</span></div>
    <div class="item" style="top:583px"><h3>2<sup style="font-size:6px">ND</sup> POINT SWEET BRISKET</h3><p style="width:80%">Brisket, Marlo’s® Sweet Raspberry BBQ Sauce and Coleslaw</p><span class="pill">$9.99</span></div>
    <div class="item" style="top:630px"><h3>1STPOINT SPICY BRISKET</h3><p style="width:80%;margin-top:6px">Brisket, Marlo’s® Sassy BBQ Sauce, Chopped Bacon, Pepperjack Cheese and Jalapenos</p><span class="pill">$10.99</span></div>
    <div class="bar split" style="position:absolute;top:685px;left:0;right:0"><div class="bar-fill">RENDEZVOUS BEACH LOADED FRIES</div><div class="bar-price">$7.99</div></div>
    <p class="intro" style="position:absolute;top:720px">Shoreline Fries with Pulled Pork, Bacon, Tomatoes, Onion, and Jalapenos smothered in White Queso and BBQ Sauce</p>
    <p class="intro" style="position:absolute;top:762px">Substitute Pork for Shredded Brisket - <b>$2.99</b></p>
  </section>

  <!-- Column 3 -->
  <section class="block" style="left:824px;top:0;width:333px;height:850px">
    <div class="bar" style="position:absolute;top:33px;left:0;right:0"><div class="bar-fill">SIDES</div></div>
    <div class="side-row" style="top:78px"><span class="name">SHORELINE FRIES</span><span class="pill">$7.49</span><span>CREAMY COLESLAW</span><span class="gap"></span><span class="pill" style="margin-right:10px">$7.49</span></div>
    <div class="side-row" style="top:99px"><span class="name">ONION RINGS</span><span class="pill">$7.49</span><span>SIDE SALAD</span><span class="gap"></span><span class="pill" style="margin-right:10px">$7.49</span></div>
    <div class="side-row" style="top:121px"><span>MAC N CHEESE BITES</span><span class="dots"></span><span class="pill" style="margin-right:10px">$7.49</span></div>
    <h2 class="shakes-title">SHAKES</h2>
    <div class="bar red" style="position:absolute;top:174px;left:0;right:0"><div class="bar-fill">MONSTER STYLE</div></div>
    <p class="intro" style="position:absolute;top:212px;width:300px">Our Monster Shakes start with our thick and creamy soft serve ice cream. We blend in handcrafted ingredients and top with whipped cream and other treats for a Monster taste! Sold as large only.</p>
    <div class="item" style="top:271px;right:10px"><h3>MARLO’S JAMMIN’ RASPBERRY</h3><p style="width:82%">Made with double raspberries and topped with Marlo’s Raspberry Jam and whipped cream.</p><span class="pill">$7.49</span></div>
    <div class="item" style="top:313px;right:10px"><h3>APPLE PIE À LA MODE</h3><p style="width:82%">An entire slice of Apple Pie blended with caramel and topped with whipped cream and caramel.</p><span class="pill">$7.49</span></div>
    <div class="item" style="top:356px;right:10px"><h3>MARLO’S JAMMIN’ RASPBERRY</h3><p style="width:82%">Made with double raspberries and topped with Marlo’s Raspberry Jam and whipped cream.</p><span class="pill">$7.49</span></div>
    <div class="item" style="top:399px;right:10px"><h3>APPLE PIE À LA MODE</h3><p style="width:82%">An entire slice of Apple Pie blended with caramel and topped with whipped cream and caramel.</p><span class="pill">$7.49</span></div>
    <div class="item" style="top:443px;right:10px"><h3>MARLO’S JAMMIN’ RASPBERRY</h3><p style="width:82%">Made with double raspberries and topped with Marlo’s Raspberry Jam and whipped cream.</p><span class="pill">$7.49</span></div>
    <div class="item" style="top:485px;right:10px"><h3>APPLE PIE À LA MODE</h3><p style="width:82%">An entire slice of Apple Pie blended with caramel and topped with whipped cream and caramel.</p><span class="pill">$7.49</span></div>
    <div class="bar red" style="position:absolute;top:529px;left:0;right:0"><div class="bar-fill">CLASSIC</div></div>
    <div class="side-row" style="top:572px"><span>WHIPPED CREAM</span><span class="dots"></span><span class="pill" style="margin-right:10px">$7.49</span></div>
    <p class="intro" style="position:absolute;top:596px;width:195px">Our Classic Shakes are made with extra creamy soft serve and served in enviornmental friendly cups. Shake flavors are as listed. No exceptions or combinations.</p>
    <div class="sizes" style="top:597px;right:10px"><div class="size"><span class="tag">SMALL</span>$4.99</div><div class="size"><span class="tag alt">LARGE</span>$6.49</div></div>
    <div class="flavours">
      <div>Famous Raspberry<br>Raspberry Cheesecake<br>Raspberry Cookies &amp; Cream<br>Raspberry Piña Colada<br>Raspberry Brownie<br>Raspberry Hazelnut<br>Raspberry Sugar Cookie<br>Raspberry Cookie Dough<br>Raspberry Marshmallow<br>Strawberry<br>Strawberry Cheesecake</div>
      <div>Strawberry Cookies &amp; Cream<br>Strawberry Brownie<br>Strawberry Hazelnut<br>Strawberry Marshmallow<br>Strawberry Cookie<br>Strawberry Chocolate<br>Piña Colada<br>Caramel<br>S’mores<br>Brownie<br>Chocolate Brownie</div>
      <div>Hazelnut Brownie<br>Caramel Brownie<br>Caramel Cookie<br>Chocolate<br>Cookies &amp; Cream<br>Cookie Dough<br>Marshmallow<br>Hazelnut<br>Candy Bar<br>PB Cup<br>Spiced Cookie</div>
    </div>
  </section>
</div>
</body>
</html>
```